Stationary for a manufacturing company
Velmoré Professional Wear
Creative Brief
Simple
John Doe
VP Sales and Marketing
123 Street Name, City Country Zip Code
example@email.com
www.example.com
Font: Hug me Tight and Neuropol Velmoré is a brand that creates professional uniforms- chefs, corporate, and etc Business card and stationary designs are up to the designers. My only comments are to make the business card: 1.) Easy to read 2.) Professional looking 3.) Clean I have uploaded photos of the logo and the shade of red used Logo should also appear in the front of the card. Also, no need to limit yourself in using the same font as the logo. Feel free to use other fonts
Use logo uploaded (side icon, red background). Red Background. Shade of red will be provided in the uploads.
sodrk sodrk
Designers Please add the company name on top of the address or wherever you think it will fit. For now, please use "Example Company, Inc."

```html
<!DOCTYPE html>
<html lang="en">
<head>
<meta charset="utf-8">
<title>Velmoré Business Card</title>
<link rel="stylesheet" href="https://fonts.googleapis.com/css2?family=Michroma&family=Orbitron:wght@400;700&family=Arimo&display=swap">
<style>
  :root {
    --stage: #000000;
    --brand-red: #b01a0a;
    --card-white: #ffffff;
    --ink-dark: #4a4a4a;
    --text-light: #ffffff;
  }
  * { margin: 0; padding: 0; box-sizing: border-box; }
  html, body { width: 1200px; height: 830px; overflow: hidden; background: var(--stage); }
  .canvas { position: relative; width: 1200px; height: 830px; background: var(--stage); }

  .card { position: absolute; top: 250px; width: 474px; height: 271px; overflow: hidden; }
  .card-front { left: 115px; background: var(--brand-red); color: var(--text-light); }
  .card-back { left: 610px; background: var(--card-white); }

  .brand-lockup { position: absolute; left: 58px; top: 28px; }
  .brand-dot { position: absolute; left: 40px; top: 0; width: 30px; height: 30px; border-radius: 50%; background: var(--text-light); }
  .brand-name { position: absolute; left: 0; top: 36px; font-family: 'Orbitron', sans-serif; font-weight: 700; font-size: 26px; white-space: nowrap; }

  .person { position: absolute; left: 58px; top: 150px; }
  .person-name { font-family: 'Michroma', sans-serif; font-size: 17px; line-height: 1.1; }
  .person-title { font-family: 'Orbitron', sans-serif; font-size: 8px; margin-top: 3px; }

  .divider { position: absolute; left: 204px; top: 122px; width: 1.5px; height: 96px; background: var(--text-light); }

  .contact-list { position: absolute; left: 220px; top: 120px; list-style: none; }
  .contact-item { display: flex; align-items: center; height: 19.5px; font-family: 'Orbitron', sans-serif; font-size: 8.5px; white-space: nowrap; }
  .contact-icon { width: 10px; height: 10px; margin-right: 5px; flex: none; }

  .swoosh { position: absolute; left: 0; top: 0; }
  .web-lockup { position: absolute; left: 318px; top: 98px; width: 120px; text-align: center; }
  .web-dot { display: block; margin: 0 auto 8px; width: 40px; height: 40px; border-radius: 50%; background: var(--brand-red); }
  .web-name { font-family: 'Orbitron', sans-serif; font-size: 16px; color: var(--brand-red); white-space: nowrap; }

  .side-label { position: absolute; top: 540px; width: 474px; text-align: center; font-family: 'Arimo', sans-serif; font-size: 38px; color: var(--text-light); }
  .label-front { left: 115px; }
  .label-back { left: 610px; }
</style>
</head>
<body>
<main class="canvas">
  <section class="card card-front" aria-label="Business card front">
    <div class="brand-lockup">
      <span class="brand-dot"></span>
      <span class="brand-name">Velmoré</span>
    </div>
    <div class="person">
      <p class="person-name">John Doe</p>
      <p class="person-title">VP Sales and Marketing</p>
    </div>
    <span class="divider"></span>
    <ul class="contact-list">
      <li class="contact-item">
        <svg class="contact-icon" viewBox="0 0 10 10"><circle cx="5" cy="5" r="5" fill="#fff"/><path d="M5 2.2a1.9 1.9 0 0 1 1.9 1.9C6.9 5.5 5 7.8 5 7.8S3.1 5.5 3.1 4.1A1.9 1.9 0 0 1 5 2.2z" fill="#b01a0a"/></svg>
        123 Street Name, City Country 1234
      </li>
      <li class="contact-item">
        <svg class="contact-icon" viewBox="0 0 10 10"><circle cx="5" cy="5" r="5" fill="#fff"/><path d="M3 2.5l1.2 0 .5 1.4-.7.6a4 4 0 0 0 1.5 1.5l.6-.7 1.4.5 0 1.2C5 7 3 5 3 2.5z" fill="#b01a0a"/></svg>
        +1-555-201346
      </li>
      <li class="contact-item">
        <svg class="contact-icon" viewBox="0 0 10 10"><circle cx="5" cy="5" r="5" fill="#fff"/><rect x="3.3" y="2" width="3.4" height="6" rx=".6" fill="#b01a0a"/></svg>
        +1-555-8047219
      </li>
      <li class="contact-item">
        <svg class="contact-icon" viewBox="0 0 10 10"><circle cx="5" cy="5" r="5" fill="#fff"/><rect x="2.5" y="3" width="5" height="4" fill="#b01a0a"/></svg>
        +1-555-3629184
      </li>
      <li class="contact-item">
        <svg class="contact-icon" viewBox="0 0 10 10"><circle cx="5" cy="5" r="5" fill="#fff"/><rect x="2.4" y="3" width="5.2" height="4" fill="#b01a0a"/><path d="M2.4 3L5 5.2 7.6 3" stroke="#fff" stroke-width=".6" fill="none"/></svg>
        example@email.com
      </li>
    </ul>
  </section>

  <section class="card card-back" aria-label="Business card back">
    <svg class="swoosh" width="474" height="271" viewBox="0 0 474 271">
      <path d="M0 0 H190 C110 30 50 120 30 271 H0 Z" fill="var(--brand-red)"/>
    </svg>
    <div class="web-lockup">
      <span class="web-dot"></span>
      <span class="web-name">Velmoré.com</span>
    </div>
  </section>

  <p class="side-label label-front">font</p>
  <p class="side-label label-back">back</p>
</main>
</body>
</html>
```